Logo alteration and design business card.

I want to make minor alterations to a logo that has already been designed and use the modified logo as part of the design of the business card.

Alterations to be made are as follows:
16-6240 TPX For the top green and bottom green dot.
16-4535 TPX For the Bottom blue and top blue dot
13-0220 TPX For the green outline.
13-5313 TPX For the middle line and the writing.

Particulars such as name, phone number and email to be generic for now so we can update and individualize them later. Website is www.orbalune.com.au

Target Market(s)

Men and Women 25-35 interested in ecofriendly/green products that have a positive vibe and message.

Industry/Entity Type

Business

Font styles to use
Script

Colors
0492cd
85cae6
00a98f
86cfc6

Requirements
Must have
• The modified Comet Hush logo.
Nice to have
• We're looking for a design that is either nature based eg. bamboo, birds, trees, water, natural scenery etc. or something eg. spacey, stars, galaxy, universe etc. a positive/happy feeling to it that is quite simple and not over loaded with imagery.

```html
<!DOCTYPE html>
<html lang="en">
<head>
<meta charset="utf-8">
<title>Comet Hush – Business Card</title>
<link href="https://fonts.googleapis.com/css2?family=Open+Sans:wght@400;600&display=swap" rel="stylesheet">
<style>
  :root {
    --backdrop: #d9d9d9;
    --ocean-deep: #1f3f9e;
    --ocean-mid: #2d62c4;
    --ocean-light: #5a8fd8;
    --leaf: #3fae1f;
    --leaf-light: #5cc734;
    --leaf-dark: #2f8f12;
    --accent-blue: #7fc6ea;
    --accent-green: #6aa51e;
    --paper: #ffffff;
    --logo-green: #8cc63f;
    --logo-blue: #1fa3d6;
    --ink-light: #ffffff;
  }
  * { margin: 0; padding: 0; box-sizing: border-box; }
  html, body { width: 1200px; height: 871px; overflow: hidden; }
  body {
    background: var(--backdrop);
    font-family: "Open Sans", Arial, sans-serif;
    position: relative;
  }
  .card {
    position: absolute;
    left: 280px;
    width: 640px;
    height: 350px;
    overflow: hidden;
    box-shadow: 0 6px 14px rgba(0,0,0,0.25);
  }
  /* Front */
  .card-front { top: 60px; }
  .front-water {
    position: absolute; inset: 0;
    background: radial-gradient(ellipse at 50% 70%, var(--ocean-light) 0%, var(--ocean-mid) 40%, var(--ocean-deep) 100%);
  }
  .front-brand {
    position: absolute; inset: 0;
    display: flex; align-items: center; justify-content: center; gap: 18px;
  }
  .brand-dot {
    width: 34px; height: 34px; border-radius: 50%;
    background: var(--logo-green);
  }
  .brand-name {
    font-size: 52px; font-weight: 600; color: var(--logo-green);
    letter-spacing: 1px;
  }
  /* Back */
  .card-back { top: 445px; background: var(--paper); }
  .back-shapes { position: absolute; inset: 0; }
  .back-brand {
    position: absolute; left: 30px; top: 140px;
    display: flex; align-items: center; gap: 12px;
  }
  .back-brand .brand-name { font-size: 40px; color: var(--logo-blue); letter-spacing: 0; }
  .back-brand .brand-dot { width: 26px; height: 26px; background: var(--logo-blue); }
  .contact {
    position: absolute; right: 34px; top: 28px;
    text-align: right; color: var(--ink-light);
  }
  .person-name { font-size: 19px; font-weight: 600; line-height: 1.2; }
  .person-role { font-size: 13px; margin-bottom: 36px; }
  .address { font-size: 13.5px; line-height: 1.5; margin-bottom: 36px; }
  .lines { list-style: none; font-size: 12.5px; line-height: 1.75; opacity: 0.92; }
  .lines li { display: flex; justify-content: flex-end; align-items: center; gap: 10px; }
  .lines svg { width: 12px; height: 12px; fill: none; stroke: var(--ink-light); stroke-width: 1.6; }
</style>
</head>
<body>

<section class="card card-front">
  <div class="front-water" role="img" aria-label="Water drop splashing into rippling blue water"></div>
  <div class="front-brand">
    <span class="brand-dot"></span>
    <span class="brand-name">Comet Hush</span>
  </div>
</section>

<section class="card card-back">
  <svg class="back-shapes" viewBox="0 0 640 350" preserveAspectRatio="none" aria-hidden="true">
    <defs>
      <linearGradient id="leafGrad" x1="0" y1="0" x2="1" y2="1">
        <stop offset="0" stop-color="var(--leaf-light)"/>
        <stop offset="1" stop-color="var(--leaf)"/>
      </linearGradient>
    </defs>
    <path d="M230 0 C330 60 345 250 225 350 L640 350 L640 0 Z" fill="var(--accent-green)"/>
    <path d="M250 0 C350 70 350 260 210 350 L640 350 L640 0 Z" fill="var(--accent-blue)"/>
    <path d="M270 0 C365 80 360 270 240 350 L640 350 L640 0 Z" fill="url(#leafGrad)" role="img" aria-label="Faint bamboo stalks and leaves pattern"/>
  </svg>

  <div class="back-brand">
    <span class="brand-dot"></span>
    <span class="brand-name">Comet Hush</span>
  </div>

  <div class="contact">
    <div class="person-name">Alex Marlow</div>
    <div class="person-role">Director</div>
    <div class="address">Fernleigh House<br>14 Willow Lane<br>Leeds LS2 7QP</div>
    <ul class="lines">
      <li>xxx - xxx - xxx
        <svg viewBox="0 0 12 12"><rect x="3" y="1" width="6" height="10" rx="1"/></svg></li>
      <li>xxx - xxx - xxx
        <svg viewBox="0 0 12 12"><path d="M1 8h10v3H1zM3 8V4h6v4M2 4c2-3 6-3 8 0"/></svg></li>
      <li>alex@orbalune.com.au
        <svg viewBox="0 0 12 12"><rect x="1" y="2.5" width="10" height="7"/><path d="M1 2.5l5 4 5-4"/></svg></li>
      <li>www.orbalune.com.au
        <svg viewBox="0 0 12 12"><circle cx="6" cy="6" r="5"/><path d="M1 6h10M6 1c-3 3-3 7 0 10M6 1c3 3 3 7 0 10"/></svg></li>
    </ul>
  </div>
</section>

</body>
</html>
```